Wordpress Design - Accounting Practice Startup

We are a relatively new Accounting Firm in Sydney with a primary focus on the Not-For-Profit sector. We need a complete re-design of our wordpress based website: www.lanternvaleledger.com.au
We already have a logo design which we would like to keep using. See uploaded files.
We have a simple menu stucture:
- Home
- About Us
- Our Services
- Contact Us
(Suggestions welcome!)
Happy for it to be a single page scrolling website linked via the menu. We would like the "Our Services" page/section to have icons for the following:
- Bookkeeping
- Payroll
- Accounting
- Training
- Consulting
- Projects
We'd like a banner at the top of the page below the menu, and a place for testimonials, possibly integrated into the body or to the side. Images and icons to be included would be great.
Our main aim is to have an elegant and modern website that works well on all devices.
Updates
Industry/Entity Type
Accounting
Colors
Designer to choose colors to be used in the design.
Look and feel
Each slider illustrates characteristics of the customer's brand and the style your logo design should communicate.

```html
<!DOCTYPE html>
<html lang="en">
<head>
<meta charset="utf-8">
<title>Lantern Vale Ledger</title>
<link href="https://fonts.googleapis.com/css2?family=Montserrat:wght@400;600;700&family=Open+Sans:wght@400;600&display=swap" rel="stylesheet">
<style>
:root{
  --green:#3f9e3a;
  --green-dark:#2f8a2b;
  --ink:#333;
  --muted:#777;
  --dark:#464646;
  --darker:#3a3a3a;
  --paper:#fff;
  --light:#f1f1f1;
}
*{box-sizing:border-box;margin:0;padding:0}
html,body{width:1200px;height:4100px;overflow:hidden;background:var(--paper)}
body{position:relative;font-family:"Open Sans",Arial,sans-serif;color:var(--ink)}
.abs{position:absolute}
h2,h3,.brand,.nav a,.btn{font-family:"Montserrat",Arial,sans-serif}

/* header */
.brand{left:66px;top:28px;font-size:40px;line-height:38px;color:var(--green);font-weight:600;display:flex;align-items:center;gap:14px}
.brand .mark{width:44px;height:44px;background:var(--green);border-radius:50%}
.brand small{display:block;font-size:30px;font-weight:400;color:#555}
.social{top:34px;left:792px;display:flex;gap:14px}
.social span{width:40px;height:40px;border-radius:50%;background:#3d3d3d}
.callnow{left:968px;top:36px;font-size:11px;color:#888;letter-spacing:1px}
.phone{left:968px;top:50px;font-size:24px;font-weight:700;color:var(--green);font-family:"Montserrat",sans-serif;display:flex;gap:6px;align-items:center}
.nav{left:0;top:112px;width:1200px;height:46px;background:var(--green)}
.nav a{position:absolute;top:0;line-height:46px;color:#fff;font-size:14px;font-weight:600;text-decoration:none}
.nav a.on{border-bottom:3px solid #2a6e27;line-height:43px}
.search{right:66px;top:8px;width:248px;height:30px;background:#fff;border-radius:2px;font-size:12px;color:#999;padding:7px 12px}

/* hero */
.hero{left:0;top:158px;width:1200px;height:607px}
.quote{left:718px;top:295px;width:389px;height:164px;background:rgba(50,50,50,.85);padding:16px 22px;color:#fff}
.quote p{font-family:"Montserrat",sans-serif;font-size:42px;line-height:46px;font-weight:400}
.quote .btn{position:absolute;right:30px;bottom:16px;background:var(--green);color:#fff;font-size:13px;padding:8px 14px}

/* about */
.about-h{left:101px;top:856px;font-size:30px;font-weight:700;color:#333}
.rule{height:3px;background:var(--green)}
.about-photo{left:101px;top:930px;width:145px;height:100px;background:linear-gradient(135deg,#8a6b4d,#c9a27a 50%,#4d4d63)}
.about-sub{left:263px;top:930px;font-size:15px;font-weight:700;font-family:"Montserrat",sans-serif}
.about-p{font-size:14px;line-height:23px;color:#888}
.more{font-size:14px;color:var(--green);font-weight:600}
.ask{left:779px;top:773px;width:325px;height:380px;background:var(--green);padding:30px 24px}
.ask h3{color:#fff;font-size:28px;font-weight:700;margin-bottom:22px}
.ask .f{background:#fff;height:44px;margin:0 0 24px;font-size:14px;color:#777;padding:12px 14px;width:260px}
.ask .go{background:#222;color:#fff;height:48px;width:260px;text-align:center;line-height:48px;font-size:16px;font-family:"Montserrat",sans-serif}

/* section titles */
.sec-title{left:0;width:1200px;text-align:center;font-size:32px;font-weight:700}
.divider{left:270px;width:660px;height:1px;background:#aaa}
.diamond{width:26px;height:26px}

/* services */
.svc{width:260px;text-align:center;color:#fff}
.svc .ic{width:124px;height:124px;border-radius:50%;background:#fff;border:8px solid var(--green);margin:0 auto;display:flex;align-items:center;justify-content:center}
.svc h3{font-size:17px;font-weight:700;margin:22px 0 14px}
.svc p{font-size:14px;line-height:23px;color:#e6e6e6;padding:0 18px}
.svc .btn{display:inline-block;margin-top:18px;background:#fff;color:#333;font-size:12px;padding:5px 12px}

/* news */
.card-t{background:var(--light);padding:56px 24px}
.card-t h4{color:var(--green);font-size:14px;font-weight:600;margin-bottom:18px}
.card-t p{font-size:13px;line-height:22px;color:#999}
.card-t .more{display:block;margin-top:8px;font-size:13px;color:#555}
.date{width:56px;height:58px;background:#555;color:#fff;font-size:12px;text-align:center;padding-top:10px;line-height:16px}
.dots span{display:inline-block;width:16px;height:16px;border-radius:50%;background:#999;margin:0 4px}

/* touch */
.field{background:var(--light);height:40px;font-size:13px;color:#888;padding:11px 16px}
.submit{left:505px;top:2910px;width:155px;height:46px;background:var(--green);color:#fff;text-align:center;line-height:46px;font-size:15px;font-weight:700}

/* contact */
.cform{left:115px;top:3635px;width:432px;height:342px;background:#f3f3f3;padding:20px 22px}
.cform h3{font-size:24px;font-weight:400;margin-bottom:18px;color:#333}
.cform .field{background:#fff;margin-bottom:12px}
.cform .sb{position:absolute;right:22px;bottom:20px;background:var(--green);color:#fff;font-size:14px;padding:10px 22px;font-family:"Montserrat",sans-serif}
.c-title{left:598px;top:3636px;color:#fff;font-size:29px;font-weight:600;font-family:"Montserrat",sans-serif}
.links li{list-style:none;color:#fff;font-size:14px;margin-bottom:26px;display:flex;gap:12px;align-items:center}
.info h5{color:#fff;font-size:18px;font-family:"Montserrat",sans-serif;font-weight:600}
.info p{color:#fff;font-size:14px;line-height:18px}
.info .pin{width:28px;height:28px;border-radius:50%;background:var(--green);display:flex;align-items:center;justify-content:center}
.footer{left:0;top:4045px;width:1200px;height:55px;background:var(--green);color:#fff;text-align:center;line-height:55px;font-size:14px}
</style>
</head>
<body>

<header>
  <div class="abs brand"><span class="mark"></span><div>LANTERN VALE<small>LEDGER</small></div></div>
  <div class="abs social" aria-label="Social links"><span></span><span></span><span></span></div>
  <div class="abs callnow">CALL US NOW</div>
  <div class="abs phone"><svg width="20" height="20" viewBox="0 0 24 24"><path d="M6.6 10.8a15 15 0 0 0 6.6 6.6l2.2-2.2a1 1 0 0 1 1-.25 11 11 0 0 0 3.6.6 1 1 0 0 1 1 1V20a1 1 0 0 1-1 1A17 17 0 0 1 3 4a1 1 0 0 1 1-1h3.5a1 1 0 0 1 1 1 11 11 0 0 0 .6 3.6 1 1 0 0 1-.25 1z" fill="#3f9e3a"/></svg>0400 555 182</div>
  <nav class="abs nav">
    <a class="on" style="left:100px">HOME</a>
    <a style="left:222px">SERVICES</a>
    <a style="left:364px">ABOUT US</a>
    <a style="left:514px">CONTACT US</a>
    <div class="abs search">Search Here...</div>
  </nav>
</header>

<section>
  <svg class="abs hero" viewBox="0 0 1200 607" role="img" aria-label="Photo of a laptop showing green charts beside a tablet on a desk">
    <defs><linearGradient id="hg" x1="0" y1="0" x2="1" y2="1"><stop offset="0" stop-color="#e8f2ee"/><stop offset=".5" stop-color="#b9d8cc"/><stop offset="1" stop-color="#7fa99a"/></linearGradient></defs>
    <polygon points="0,0 1200,0 1200,330 380,607 0,607" fill="url(#hg)"/>
  </svg>
  <div class="abs quote"><p>“EVERY NUMBER<br>COUNTS...”</p><span class="btn">READ MORE</span></div>
</section>

<section id="about">
  <h2 class="abs about-h">ABOUT LANTERN VALE LEDGER</h2>
  <div class="abs rule" style="left:101px;top:900px;width:66px"></div>
  <div class="abs about-photo" role="img" aria-label="Photo of a team meeting around a table"></div>
  <div class="abs about-sub">WHAT ARE OUR ADVANTAGES?</div>
  <p class="abs about-p" style="left:263px;top:956px;width:420px">At Lantern Vale Ledger, we believe that every number counts. We strive to deliver a premium service at a reasonable cost.</p>
  <p class="abs about-p" style="left:101px;top:1040px;width:560px">We strive to deliver a premium service at a reasonable cost. Our focus is to ensure your financial needs are met with the quality, integrity, diligence and time-lines that you would expect.</p>
  <div class="abs more" style="left:101px;top:1136px">Read More →</div>
  <form class="abs ask">
    <h3>HAVE A QUESTION?</h3>
    <div class="f">Your Name</div><div class="f">Your Email</div><div class="f">Phone No.</div>
    <div class="go">GET STARTED</div>
  </form>
</section>

<section id="services">
  <svg class="abs" style="left:0;top:1257px" width="1200" height="648" viewBox="0 0 1200 648"><polygon points="0,96 1200,0 1200,566 0,648" fill="var(--dark)"/>
    <polyline points="26,330 14,342 26,354" fill="none" stroke="#ccc" stroke-width="3"/>
    <polyline points="1174,330 1186,342 1174,354" fill="none" stroke="#ccc" stroke-width="3"/></svg>
  <h2 class="abs sec-title" style="top:1350px;color:#fff">OUR SERVICES</h2>
  <div class="abs divider" style="top:1413px;background:#888"></div>
  <svg class="abs diamond" style="left:587px;top:1400px" viewBox="0 0 26 26"><rect x="6" y="6" width="14" height="14" transform="rotate(45 13 13)" fill="#fff"/></svg>

  <div class="abs svc" style="left:50px;top:1474px"><div class="ic"><svg width="60" height="60" viewBox="0 0 60 60"><rect x="8" y="10" width="12" height="40" fill="#3f9e3a"/><rect x="24" y="10" width="12" height="40" fill="#3f9e3a"/><rect x="40" y="10" width="12" height="40" fill="#555"/></svg></div><h3>BOOKKEEPING</h3><p>Estate planning is a process that involves examining your assets and liabilities, your personal and extended estate.</p><span class="btn">Read more →</span></div>
  <div class="abs svc" style="left:337px;top:1474px"><div class="ic"><svg width="60" height="60" viewBox="0 0 60 60"><circle cx="30" cy="22" r="14" fill="#3f9e3a"/><text x="30" y="29" text-anchor="middle" font-size="18" font-weight="700" fill="#fff" font-family="Montserrat,sans-serif">$</text><path d="M6 46h18l10 4 16-8v6l-16 8-28-2z" fill="#3f9e3a"/></svg></div><h3>PAYROLL</h3><p>Estate planning is a process that involves examining your assets and liabilities, your personal and extended estate.</p><span class="btn">Read more →</span></div>
  <div class="abs svc" style="left:613px;top:1474px"><div class="ic"><svg width="60" height="60" viewBox="0 0 60 60"><rect x="14" y="6" width="32" height="48" rx="3" fill="#3f9e3a"/><rect x="19" y="12" width="22" height="9" fill="#fff"/><g fill="#fff"><rect x="19" y="26" width="6" height="6"/><rect x="27" y="26" width="6" height="6"/><rect x="35" y="26" width="6" height="6"/><rect x="19" y="35" width="6" height="6"/><rect x="27" y="35" width="6" height="6"/><rect x="35" y="35" width="6" height="6"/></g></svg></div><h3>ACCOUNTING</h3><p>Estate planning is a process that involves examining your assets and liabilities, your personal and extended estate.</p><span class="btn">Read more →</span></div>
  <div class="abs svc" style="left:890px;top:1474px"><div class="ic"><svg width="60" height="60" viewBox="0 0 60 60"><rect x="10" y="8" width="40" height="30" fill="none" stroke="#3f9e3a" stroke-width="4"/><polyline points="16,32 24,24 30,28 42,16" fill="none" stroke="#3f9e3a" stroke-width="3"/><line x1="30" y1="38" x2="22" y2="54" stroke="#3f9e3a" stroke-width="4"/><line x1="30" y1="38" x2="38" y2="54" stroke="#3f9e3a" stroke-width="4"/></svg></div><h3>TRAINING</h3><p>Estate planning is a process that involves examining your assets and liabilities, your personal and extended estate.</p><span class="btn">Read more →</span></div>
</section>

<section id="news">
  <h2 class="abs sec-title" style="top:1940px">KNOWLEDGE AND NEWS</h2>
  <div class="abs divider" style="top:2004px"></div>
  <svg class="abs diamond" style="left:587px;top:1991px" viewBox="0 0 26 26"><rect x="6" y="6" width="14" height="14" transform="rotate(45 13 13)" fill="#222"/></svg>

  <div class="abs card-t" style="left:96px;top:2110px;width:254px;height:246px"><h4>Real estate laws on the move</h4><p>There are many variations of passages of Lorem Ipsum available majority have suffered...</p><span class="more">Read More ⟶</span></div>
  <div class="abs" style="left:350px;top:2110px;width:235px;height:246px;background:linear-gradient(160deg,#c7d3de,#5a6d80 60%,#2c3a48)" role="img" aria-label="Photo of city office towers seen from below"></div>
  <div class="abs date" style="left:350px;top:2110px">29<br>NOV</div>

  <div class="abs card-t" style="left:615px;top:2110px;width:260px;height:246px"><h4>Real estate laws on the move</h4><p>If people are really excited about their music, and that's their primary motivation...</p><span class="more">Read More ⟶</span></div>
  <div class="abs" style="left:875px;top:2110px;width:232px;height:246px;background:linear-gradient(180deg,#f4f4f4,#d8d8d8 50%,#3a3a3a)" role="img" aria-label="Photo of two businessmen in suits talking"></div>
  <div class="abs date" style="left:875px;top:2110px">29<br>NOV</div>

  <div class="abs dots" style="left:560px;top:2410px"><span style="background:var(--green)"></span><span></span><span></span></div>
</section>

<section id="contact-form">
  <svg class="abs" style="left:0;top:2474px" width="1200" height="560" viewBox="0 0 1200 560"><polygon points="0,136 600,0 1200,136 1200,560 0,560" fill="#f0f0f0"/></svg>
  <h2 class="abs sec-title" style="top:2566px">GET IN TOUCH</h2>
  <div class="abs divider" style="top:2630px"></div>
  <svg class="abs diamond" style="left:587px;top:2617px" viewBox="0 0 26 26"><rect x="6" y="6" width="14" height="14" transform="rotate(45 13 13)" fill="#222"/></svg>
  <p class="abs" style="left:0;width:1200px;text-align:center;top:2668px;font-size:14px;color:#444">Fill out the form below to get in touch. A Lantern Vale team member will be in touch shortly!</p>
  <div class="abs field" style="left:132px;top:2720px;width:446px;background:#fff">Full Name</div>
  <div class="abs field" style="left:132px;top:2780px;width:446px;background:#fff">Email Address</div>
  <div class="abs field" style="left:132px;top:2838px;width:446px;background:#fff">Phone Number</div>
  <div class="abs field" style="left:608px;top:2720px;width:446px;height:154px;background:#fff">Your Message</div>
  <div class="abs submit">SUBMIT</div>
</section>

<div class="abs" style="left:0;top:3034px;width:1200px;height:424px;background:linear-gradient(135deg,#e6e6e6,#d4d4d4 60%,#cfe3cf)" role="img" aria-label="Street map showing the office location"></div>

<section id="contact">
  <div class="abs" style="left:0;top:3458px;width:1200px;height:587px;background:linear-gradient(180deg,var(--dark),var(--darker))"></div>
  <h2 class="abs sec-title" style="top:3490px;color:#fff">CONTACT US</h2>
  <div class="abs divider" style="top:3573px;background:#888"></div>
  <svg class="abs diamond" style="left:587px;top:3560px" viewBox="0 0 26 26"><rect x="6" y="6" width="14" height="14" transform="rotate(45 13 13)" fill="#fff"/></svg>

  <form class="abs cform">
    <h3>Contact form</h3>
    <div class="field">Name</div><div class="field">Email</div><div class="field" style="height:86px">Message</div>
    <span class="sb">SUBMIT</span>
  </form>

  <div class="abs c-title">A Full Service Technology Company.</div>
  <ul class="abs links" style="left:598px;top:3700px">
    <li><svg width="14" height="12" viewBox="0 0 14 12"><polyline points="1,6 5,10 13,1" fill="none" stroke="#3f9e3a" stroke-width="2.5"/></svg>Home</li>
    <li><svg width="14" height="12" viewBox="0 0 14 12"><polyline points="1,6 5,10 13,1" fill="none" stroke="#3f9e3a" stroke-width="2.5"/></svg>Services</li>
    <li><svg width="14" height="12" viewBox="0 0 14 12"><polyline points="1,6 5,10 13,1" fill="none" stroke="#3f9e3a" stroke-width="2.5"/></svg>About Us</li>
    <li><svg width="14" height="12" viewBox="0 0 14 12"><polyline points="1,6 5,10 13,1" fill="none" stroke="#3f9e3a" stroke-width="2.5"/></svg>Contact Us</li>
  </ul>
  <div class="abs brand" style="left:598px;top:3900px;color:#ccc;font-size:34px;line-height:32px"><div>LANTERN VALE<small style="color:#ccc;font-size:26px">LEDGER</small></div></div>

  <div class="abs info" style="left:896px;top:3700px"><h5>Address</h5><p>Mara Quill<br>Principal Consultant</p></div>
  <div class="abs info" style="left:896px;top:3800px;display:flex;gap:10px"><span class="pin"><svg width="14" height="14" viewBox="0 0 24 24"><path d="M6.6 10.8a15 15 0 0 0 6.6 6.6l2.2-2.2a1 1 0 0 1 1-.25 11 11 0 0 0 3.6.6 1 1 0 0 1 1 1V20a1 1 0 0 1-1 1A17 17 0 0 1 3 4a1 1 0 0 1 1-1h3.5a1 1 0 0 1 1 1 11 11 0 0 0 .6 3.6 1 1 0 0 1-.25 1z" fill="#fff"/></svg></span><div><h5>Phone</h5><p>+0400 555 182<br>0400 555 917</p></div></div>
  <div class="abs info" style="left:896px;top:3888px;display:flex;gap:10px"><span class="pin"><svg width="14" height="12" viewBox="0 0 16 12"><rect x="1" y="1" width="14" height="10" fill="none" stroke="#fff" stroke-width="1.6"/><polyline points="1,1 8,7 15,1" fill="none" stroke="#fff" stroke-width="1.6"/></svg></span><div><h5>Email</h5><p>mara@lanternvaleledger.com.au<br>team@lanternvaleledger.com.au</p></div></div>
  <div class="abs info" style="left:896px;top:3718px;display:none"></div>
  <div class="abs" style="left:896px;top:3760px"><span class="pin" style="display:none"></span></div>
</section>

<footer class="abs footer">© Lantern Vale Ledger 2016. All rights reserved.</footer>

</body>
</html>
```